Flyer Design Project for lawn care business

I need a flyer designed for my lawn care business, "Ashby's Groundcare Services".  It is a family owned small landscaping company. I was thinking something that I can print  2- 3 per page.
I have  2 different logos I can upload to give an idea.  I have seen some I like that are colorfull with neat graphics but I also like some that are simple and elegant.  I would like something that catches your eye and looks professionaly done.

Target Market(s)
Homeowners in Durham, North Carolina with homes usually valued $200,000 or more.
Industry/Entity Type
Landscaping
Requirements
Must have
- I would like the address of my website listed on it, www.ashbygroundcareservices.com
I would like for it to say somewhere, 50% off first service with seasonal service.
Not sure if I want to list some of the services that I offer or just say full service lawn care.
Nice to have
- I have a logo with a bull pushing a lawn mower.  I live in Durham, NC also known as the Bull City.  I am not in love with the logo so feel free to change it or not use it at all.

```html
<!DOCTYPE html>
<html lang="en">
<head>
<meta charset="utf-8">
<title>Ashby's Groundcare Services – Flyer</title>
<link href="https://fonts.googleapis.com/css2?family=Passion+One:wght@400;700&family=Oswald:wght@500&family=Arimo:wght@700&display=swap" rel="stylesheet">
<style>
  :root {
    --page-bg: #e9e9e7;
    --lawn-light: #5fd13a;
    --lawn-mid: #2fb51f;
    --lawn-dark: #1d8f14;
    --sun-yellow: #f6e500;
    --leaf-green: #6cb52d;
    --badge-text: #58a82a;
    --white: #ffffff;
    --navy: #24406e;
    --tag-orange: #e7961d;
  }
  * { margin: 0; padding: 0; box-sizing: border-box; }
  html, body {
    width: 1200px; height: 731px; overflow: hidden;
    background: var(--page-bg);
  }
  .flyer {
    position: absolute; left: 40px; top: 99px;
    width: 1120px; height: 533px;
    background: var(--white);
    box-shadow: 0 2px 6px rgba(0,0,0,.15);
    overflow: hidden;
  }
  .hero {
    position: absolute; left: 0; top: 0; width: 1120px; height: 392px;
  }
  .hero-photo {
    position: absolute; inset: 0;
    background: radial-gradient(ellipse at 30% 20%, var(--lawn-light) 0%, var(--lawn-mid) 55%, var(--lawn-dark) 100%);
  }
  .brand-title {
    position: absolute; left: 38px; top: 146px;
    font-family: "Passion One", sans-serif; font-weight: 700;
    color: var(--sun-yellow);
    font-size: 146px; line-height: 1; letter-spacing: 2px;
  }
  .brand-subtitle {
    position: absolute; left: 40px; top: 296px;
    font-family: "Passion One", sans-serif; font-weight: 400;
    color: var(--sun-yellow);
    font-size: 56px; line-height: 1; letter-spacing: 2px;
  }
  .service-list {
    position: absolute; left: 630px; top: 28px;
    list-style: none;
    font-family: "Oswald", sans-serif; font-weight: 500;
    color: var(--white);
    font-size: 42px; line-height: 46px; text-transform: uppercase;
  }
  .service-list li { position: relative; padding-left: 26px; margin-bottom: 12px; }
  .service-list li::before {
    content: ""; position: absolute; left: 2px; top: 16px;
    width: 11px; height: 11px; border-radius: 50%; background: var(--white);
  }
  .offer-badge { position: absolute; left: 857px; top: 61px; width: 252px; height: 252px; }
  .offer-text {
    position: absolute; left: 867px; top: 96px; width: 232px;
    text-align: center; color: var(--badge-text);
    font-family: "Arimo", sans-serif; font-weight: 700;
  }
  .offer-amount { font-size: 68px; line-height: 58px; letter-spacing: -1px; }
  .offer-terms { font-size: 22px; line-height: 25px; margin-top: 4px; }
  .contact-band { position: absolute; left: 0; top: 392px; width: 1120px; height: 141px; background: var(--white); }
  .logo-lockup { position: absolute; left: 38px; top: 22px; }
  .logo-square { position: absolute; left: 0; top: 4px; width: 64px; height: 64px; background: var(--leaf-green); }
  .logo-name {
    position: absolute; left: 78px; top: 2px; width: 220px;
    font-family: "Passion One", sans-serif; font-weight: 700;
    color: var(--leaf-green); font-size: 32px; line-height: 34px; white-space: nowrap;
  }
  .logo-tagline {
    position: absolute; left: 0; top: 80px; white-space: nowrap;
    font-family: "Oswald", sans-serif; font-weight: 500;
    color: var(--leaf-green); font-size: 11px; letter-spacing: .5px;
  }
  .logo-phone {
    position: absolute; left: 250px; top: 78px; white-space: nowrap;
    font-family: "Oswald", sans-serif; font-weight: 500;
    color: var(--tag-orange); font-size: 13px;
  }
  .phone-number {
    position: absolute; left: 442px; top: 18px;
    font-family: "Arimo", sans-serif; font-weight: 700;
    color: var(--leaf-green); font-size: 68px; line-height: 1; letter-spacing: 1px;
  }
  .find-us {
    position: absolute; left: 960px; top: 44px;
    font-family: "Oswald", sans-serif; font-weight: 500;
    color: var(--navy); font-size: 22px; line-height: 1;
  }
  .find-us-dot {
    position: absolute; left: 1050px; top: 36px;
    width: 38px; height: 38px; border-radius: 50%; background: var(--navy);
  }
  .web-address {
    position: absolute; left: 442px; top: 94px;
    font-family: "Arimo", sans-serif; font-weight: 700;
    color: var(--leaf-green); font-size: 29px; line-height: 1;
  }
</style>
</head>
<body>
  <main class="flyer">
    <section class="hero">
      <div class="hero-photo" role="img" aria-label="Photo of a person pushing a red lawn mower across a bright green lawn"></div>
      <h1 class="brand-title">Ashby’s</h1>
      <p class="brand-subtitle">Groundcare Services</p>
      <ul class="service-list">
        <li>Landscaping<br>Services</li>
        <li>Plumbing<br>Services</li>
        <li>HVAC</li>
        <li>Carpentry</li>
      </ul>
      <svg class="offer-badge" viewBox="0 0 252 252" aria-hidden="true">
        <circle cx="126" cy="126" r="122" fill="none" stroke="var(--sun-yellow)" stroke-width="3"/>
        <circle cx="126" cy="126" r="114" fill="var(--sun-yellow)"/>
      </svg>
      <div class="offer-text">
        <div class="offer-amount">50%<br>OFF</div>
        <div class="offer-terms">first service<br>with seasonal<br>service</div>
      </div>
    </section>
    <section class="contact-band">
      <div class="logo-lockup">
        <div class="logo-square"></div>
        <div class="logo-name">Ashby’s<br>Groundcare Services</div>
        <div class="logo-tagline">Carpentry • Plumbing • HVAC • Lawn Care</div>
        <div class="logo-phone">(919) 555-0147</div>
      </div>
      <div class="phone-number">919-555-0147</div>
      <div class="find-us">FIND US</div>
      <div class="find-us-dot"></div>
      <div class="web-address">www.ashbygroundcareservices.com</div>
    </section>
  </main>
</body>
</html>
```